Start up Events company needs a business card design

We are a brand new start up events company that need an impressively designed business card to make the best first impression with our future clients.

Description on company:
- start-up company
- in the events management industry
- selling flagship children related event
- our future clients will mostly be vendors in the alternative education industry. dance schools, music schools, sports camp facilitators, academic establishments
- our target market are kids, parents of kids, mass market

What we need in the business card:
- we currently have a rough design that I have uploaded. we need to brush it up. make it look more professional, more vibrant but keep the meaning of the company which is called "Kite & Lantern"
- a reason for the "Kite & Lantern" concept is because we will be starting off with a flagship event & be branching out into all other related businesses relating to our core highlight which is kids & alternative education.
- this is a tentative logo we have selected - which is a girl on a swing. to represent momentum as a start up company and related to children
- if you have a better logo alternative, please do suggest it to us
- we need more colours, vibrancy yet it has to be sleek and professional.

As we are a start-up company, our budget is tight. If you have a good idea / concept, do take on this project overlooking the tight budget.
If you require any additional information, do feel free to drop us messages!

Thank you designers!

```html
<!DOCTYPE html>
<html lang="en">
<head>
<meta charset="utf-8">
<title>Kite &amp; Lantern — Business Card</title>
<link rel="stylesheet" href="https://fonts.googleapis.com/css2?family=Cinzel:wght@500&family=Mulish:wght@400;700&display=swap">
<style>
  :root {
    --backdrop: #c9e7dd;
    --teal: #5ec8c0;
    --teal-light: #72d2cb;
    --teal-deep: #4fbab2;
    --paper: #ffffff;
    --ink-light: #ffffff;
    --spoke: #c9cccc;
    --dot-person: #b6d64a;
    --dot-phone: #e0463d;
    --dot-mail: #8a5bb8;
    --icon-ink: #333333;
  }
  * { box-sizing: border-box; margin: 0; padding: 0; }
  html, body { width: 1200px; height: 856px; overflow: hidden; }
  body {
    background: var(--backdrop);
    font-family: "Mulish", Arial, sans-serif;
    position: relative;
  }
  .card {
    position: absolute;
    width: 520px;
    height: 300px;
    border-radius: 34px;
    overflow: hidden;
    background: linear-gradient(160deg, var(--teal-light), var(--teal-deep));
    box-shadow: 0 10px 24px rgba(40, 110, 100, 0.18);
  }
  .card--back { left: 520px; top: 90px; }
  .card--front { left: 150px; top: 440px; }

  /* Back side */
  .back__brand {
    position: absolute;
    left: 150px; top: 50px;
    display: flex; align-items: center; gap: 14px;
    color: var(--ink-light);
  }
  .back__mark {
    width: 46px; height: 46px; border-radius: 50%;
    background: var(--paper);
    flex: none;
  }
  .back__name {
    font-family: "Cinzel", Georgia, serif;
    font-weight: 500;
    font-size: 24px;
    line-height: 1;
    white-space: nowrap;
  }
  .back__tagline {
    font-size: 16px;
    margin-top: 4px;
    white-space: nowrap;
  }
  .back__quote {
    position: absolute;
    left: 36px; right: 36px; top: 138px;
    text-align: center;
    color: var(--ink-light);
    font-size: 12.5px;
    line-height: 1.55;
    letter-spacing: 0.2px;
  }
  .back__author {
    position: absolute;
    right: 44px; top: 252px;
    color: var(--ink-light);
    font-size: 12px;
  }

  /* Front side */
  .front__panel {
    position: absolute;
    left: -230px; top: -120px;
    width: 570px; height: 570px;
    border-radius: 50%;
    background: var(--paper);
  }
  .front__brand {
    position: absolute;
    left: 40px; top: 58px;
    font-family: "Cinzel", Georgia, serif;
    font-weight: 500;
    font-size: 26px;
    color: var(--teal-deep);
    white-space: nowrap;
  }
  .front__spokes {
    position: absolute;
    left: 0; top: 0;
  }
  .front__emblem {
    position: absolute;
    left: 78px; top: 106px;
    width: 172px; height: 172px;
    border-radius: 50%;
    background: var(--teal);
  }
  .front__dots {
    position: absolute;
    left: 0; top: 0;
  }
  .front__details {
    position: absolute;
    left: 350px; top: 74px;
    color: var(--ink-light);
    white-space: nowrap;
  }
  .front__person { font-size: 16px; line-height: 1.2; }
  .front__person b { font-weight: 700; }
  .front__role { font-size: 12px; font-weight: 400; }
  .front__contact { font-size: 13px; margin-top: 14px; line-height: 1.75; }
</style>
</head>
<body>

  <section class="card card--back" aria-label="Card back">
    <div class="back__brand">
      <span class="back__mark"></span>
      <div>
        <div class="back__name">Kite &amp; Lantern</div>
        <div class="back__tagline">Personalizing education</div>
      </div>
    </div>
    <p class="back__quote">“The key to this transformation is not to standardize education, but to personalize it, to build achievement on discovering the individual talents of each child, to put students in an environment where they want to learn and where they can naturally discover their true passions.”</p>
    <span class="back__author">-Ada Linwood</span>
  </section>

  <section class="card card--front" aria-label="Card front">
    <div class="front__panel"></div>
    <div class="front__brand">Kite &amp; Lantern</div>

    <svg class="front__spokes" width="520" height="300" viewBox="0 0 520 300" aria-hidden="true">
      <g stroke="var(--spoke)" stroke-width="9" stroke-linecap="round">
        <line x1="220" y1="150" x2="320" y2="86"/>
        <line x1="228" y1="172" x2="330" y2="114"/>
        <line x1="232" y1="194" x2="336" y2="142"/>
      </g>
    </svg>

    <div class="front__emblem"></div>

    <svg class="front__dots" width="520" height="300" viewBox="0 0 520 300" aria-hidden="true">
      <circle cx="320" cy="86" r="10" fill="var(--paper)"/>
      <circle cx="320" cy="86" r="7.5" fill="var(--dot-person)"/>
      <circle cx="320" cy="84" r="2.2" fill="var(--icon-ink)"/>
      <path d="M316.5 90.5 a3.5 3.5 0 0 1 7 0 z" fill="var(--icon-ink)"/>

      <circle cx="330" cy="114" r="10" fill="var(--paper)"/>
      <circle cx="330" cy="114" r="7.5" fill="var(--dot-phone)"/>
      <rect x="327.3" y="109.5" width="5.4" height="9" rx="1" fill="none" stroke="var(--icon-ink)" stroke-width="1.2"/>

      <circle cx="336" cy="142" r="10" fill="var(--paper)"/>
      <circle cx="336" cy="142" r="7.5" fill="var(--dot-mail)"/>
      <rect x="332" y="139" width="8" height="6" fill="none" stroke="var(--icon-ink)" stroke-width="1.1"/>
      <path d="M332 139 l4 3 l4 -3" fill="none" stroke="var(--icon-ink)" stroke-width="1.1"/>
    </svg>

    <div class="front__details">
      <div class="front__person"><b>Clara Wen</b> <span class="front__role">| Co-founder</span></div>
      <div class="front__contact">
        <div>9000 4821</div>
        <div>hello@kitelantern.com</div>
      </div>
    </div>
  </section>

</body>
</html>
```